Brightfield Optics seeks updated contemporary business card

Brightfield Optics utilizes advanced technology and we take pride in the modern look and feel of our practice. We like our current card, but it's been four years so it is time for an update.

Target Market(s)

Females 25-45 make the most health care decisions for their family.

Contact Information for Business Card

Clean front. Back with info and with empty space for appointment time or other small note

Requirements
Must have
• Logo
Ridge Marketvale, 28413 E Larkspur Ave
Cedar Terrace Marketvale, 4638 S Dunmore Rd
Call or text: 509-342-1968
email: hello@brightfieldoptics.example
brightfieldoptics.example
Dr Tobias Werring & Associates

```html
<!DOCTYPE html>
<html lang="en">
<head>
<meta charset="utf-8">
<title>Brightfield Optics – Business Card</title>
<link rel="stylesheet" href="https://fonts.googleapis.com/css2?family=Montserrat:wght@600;700&family=Questrial&display=swap">
<style>
  :root {
    --backdrop: #c6c6c6;
    --card-dark: #2e2e2e;
    --card-light: #f7f7f7;
    --accent: #0099d6;
    --band-grey: #a6a6a4;
    --ink-light: #ffffff;
    --ink-dark: #333333;
    --rule: #3a3a3a;
  }
  * { margin: 0; padding: 0; box-sizing: border-box; }
  html, body { width: 960px; height: 1200px; overflow: hidden; }
  body { background: var(--backdrop); position: relative; font-family: "Questrial", sans-serif; }

  .card { position: absolute; left: 42px; width: 876px; height: 526px; overflow: hidden; }
  .card-front { top: 45px; background: var(--card-dark); color: var(--ink-light); }
  .card-back { top: 629px; background: var(--card-light); color: var(--ink-dark); }

  .name-block { position: absolute; left: 76px; top: 117px; padding-left: 11px; border-left: 5px solid var(--accent); }
  .name { font-family: "Montserrat", sans-serif; font-weight: 600; font-size: 31px; line-height: 34px; letter-spacing: -0.5px; }
  .associates { font-family: "Questrial", sans-serif; font-size: 19px; line-height: 20px; }

  .brand { position: absolute; left: 580px; top: 138px; display: flex; align-items: center; gap: 12px; }
  .brand-mark { width: 22px; height: 22px; border-radius: 50%; background: var(--accent); }
  .brand-name { font-family: "Questrial", sans-serif; font-size: 27px; color: var(--accent); }

  .contact-list { position: absolute; left: 77px; top: 267px; list-style: none; }
  .contact-item { display: flex; align-items: center; height: 32px; margin-bottom: 13px; font-size: 23px; }
  .icon { width: 32px; height: 32px; border-radius: 3px; background: var(--accent); display: flex; align-items: center; justify-content: center; margin-right: 20px; }
  .icon svg { width: 20px; height: 20px; }

  .band-grey { position: absolute; left: 575px; top: 405px; width: 301px; height: 61px; background: var(--band-grey); clip-path: polygon(0 0, 100% 0, 100% 100%, 49px 100%); }
  .band-accent { position: absolute; left: 0; top: 405px; width: 620px; height: 61px; background: var(--accent); clip-path: polygon(0 0, 572px 0, 620px 100%, 0 100%); display: flex; align-items: center; padding-left: 77px; font-size: 22px; }
  .band-accent .icon { background: var(--ink-light); width: 31px; height: 31px; margin-right: 22px; }

  .side-stripe { position: absolute; left: 0; top: 0; width: 14px; height: 100%; background: linear-gradient(var(--accent) 0 166px, var(--card-dark) 166px 360px, var(--accent) 360px); }
  .appointment { position: absolute; left: 117px; top: 80px; width: 643px; }
  .appointment h2 { font-family: "Montserrat", sans-serif; font-weight: 700; font-size: 31px; line-height: 38px; text-align: center; margin-bottom: 20px; }
  .field { font-size: 22px; line-height: 26px; border-bottom: 2px solid var(--rule); height: 28px; margin-bottom: 27px; }
  .days { position: relative; font-size: 22px; line-height: 26px; height: 28px; margin-bottom: 27px; }
  .days span { position: absolute; top: 0; }
  .days span:nth-child(1) { left: 0; }
  .days span:nth-child(2) { left: 67px; }
  .days span:nth-child(3) { left: 148px; }
  .days span:nth-child(4) { left: 232px; }
  .days span:nth-child(5) { left: 318px; }
  .days span:nth-child(6) { left: 413px; }
  .days span:nth-child(7) { left: 475px; }
  .days span:nth-child(8) { left: 548px; }
  .note { font-size: 22px; line-height: 27px; text-align: center; margin-top: -4px; }
</style>
</head>
<body>
  <section class="card card-front">
    <div class="name-block">
      <div class="name">Dr Tobias Werring</div>
      <div class="associates">&amp; Associates</div>
    </div>

    <div class="brand">
      <span class="brand-mark"></span>
      <span class="brand-name">Brightfield Optics</span>
    </div>

    <ul class="contact-list">
      <li class="contact-item">
        <span class="icon"><svg viewBox="0 0 24 24"><path fill="#fff" d="M6.6 10.8a15 15 0 0 0 6.6 6.6l2.2-2.2a1 1 0 0 1 1-.25 11.4 11.4 0 0 0 3.6.57 1 1 0 0 1 1 1V20a1 1 0 0 1-1 1A17 17 0 0 1 3 4a1 1 0 0 1 1-1h3.5a1 1 0 0 1 1 1c0 1.25.2 2.45.57 3.57a1 1 0 0 1-.25 1z"/></svg></span>
        509-342-1968
      </li>
      <li class="contact-item">
        <span class="icon"><svg viewBox="0 0 24 24"><rect x="3" y="6" width="18" height="12" fill="none" stroke="#fff" stroke-width="1.6"/><path d="M3 6l9 7 9-7M3 18l7-6M21 18l-7-6" fill="none" stroke="#fff" stroke-width="1.4"/></svg></span>
        hello@brightfieldoptics.example
      </li>
      <li class="contact-item">
        <span class="icon"><svg viewBox="0 0 24 24" fill="none" stroke="#fff" stroke-width="1.5"><circle cx="12" cy="12" r="9"/><ellipse cx="12" cy="12" rx="4" ry="9"/><path d="M3 12h18M4.5 7.5h15M4.5 16.5h15"/></svg></span>
        brightfieldoptics.example
      </li>
    </ul>

    <div class="band-grey"></div>
    <div class="band-accent">
      <span class="icon"><svg viewBox="0 0 24 24"><path d="M3 12l9-8 9 8" fill="none" stroke="#0099d6" stroke-width="2.4"/><path d="M6 11v9h4.5v-5h3v5H18v-9" fill="none" stroke="#0099d6" stroke-width="2.2"/></svg></span>
      Larkspur Valley, Cedar Terrace Marketvale
    </div>
  </section>

  <section class="card card-back">
    <div class="side-stripe"></div>
    <div class="appointment">
      <h2>Appointment</h2>
      <div class="field">Name:</div>
      <div class="field">Date:</div>
      <div class="days"><span>On:</span><span>Mon.</span><span>Tues.</span><span>Wed.</span><span>Thurs.</span><span>Fri.</span><span>Sat.</span><span>Sun.</span></div>
      <div class="field">Time:</div>
      <p class="note">If you are unable to make your appointment, please call us<br>to reschedule.</p>
    </div>
  </section>
</body>
</html>
```